Craft Beer Can Label Design needed to update existing bottle label

We need an existing bottle label design changed and updated to a can label.I have attached 2 can ideas that i really love and also attached our existing bottle label, if you could have the same wording, barcodes and description of the bottle label (kelmoor lager) and change to look similar to the can designs.

The can dimensions will be different to the existing bottle label.
New can label dimensions-
Height= 88mm
Wide= 205mm

Target Market(s)

beer lovers

Colors

Designer to choose colors to be used in the design.

Requirements
Must have
• all the information on the existing Kelmoor Lager label which is in the design brief
• Also want to add the silver can colour like in the middle of the tansford brewing can so that it blends in with the can, as this is a label over the silver can and not a printed can.
Nice to have
• the same design concepts as the attached other 2 can designs
Should not have
• do not just copy the other cans, need to make it look original

```html
<!DOCTYPE html>
<html lang="en">
<head>
<meta charset="utf-8">
<title>Kelmoor Lager – Can Label Concepts</title>
<link rel="stylesheet" href="https://fonts.googleapis.com/css2?family=Oswald:wght@500;600;700&family=Arimo:wght@400;700&family=Montserrat:wght@600&display=swap">
<style>
:root{
  --ink:#1c1c1c;
  --yellow:#f2cf00;
  --paper:#eceef0;
  --paper-soft:#f3f4f5;
  --white:#ffffff;
  --map:#d3d6da;
}
*{margin:0;padding:0;box-sizing:border-box}
html,body{width:881px;height:1200px;overflow:hidden;background:var(--white)}
body{position:relative;font-family:"Arimo",Arial,sans-serif;color:var(--ink)}

.label{position:absolute;left:57px;width:767px;height:329px;overflow:hidden;background:var(--paper)}
.label--one{top:46px}
.label--two{top:413px}
.label--three{top:781px}

/* backgrounds */
.texture{position:absolute;left:0;top:0;width:767px;height:260px}
.texture--water{background:linear-gradient(135deg,#e6e8ea,#f1f2f3 40%,#e4e6e8 70%,#eff0f1)}
.texture--plain{background:var(--paper-soft)}
.texture--tiles{background:linear-gradient(160deg,#e9ebed,#f4f5f6 50%,#e6e8ea)}
.halftone{position:absolute;left:283px;top:35px;width:200px;height:185px;border-radius:50%;
  background:radial-gradient(circle,rgba(140,140,140,.35) 0%,rgba(160,160,160,.18) 55%,rgba(236,238,240,0) 72%)}

/* base band */
.rule{position:absolute;left:0;top:257px;width:767px;height:4px;background:var(--ink)}
.stripe{position:absolute;left:0;top:261px;width:767px;height:6px;background:var(--yellow)}
.band{position:absolute;left:0;top:267px;width:767px;height:62px;background:var(--ink)}
.band--marble{background:linear-gradient(100deg,#1c1c1c 0%,#3a3222 18%,#1c1c1c 32%,#4a3d22 50%,#1c1c1c 66%,#3f3520 84%,#1c1c1c 100%)}
.notch{position:absolute;left:370px;top:248px;width:0;height:0;border-left:13px solid transparent;border-right:13px solid transparent;border-bottom:13px solid var(--yellow)}
.chevron{position:absolute;left:346px;top:0}

/* ingredients */
.ingredients{position:absolute;left:33px;top:30px;display:flex}
.ingredient{width:45px;display:flex;flex-direction:column;align-items:center;position:relative}
.ingredient + .ingredient::before{content:"";position:absolute;left:0;top:2px;height:42px;border-left:1px dashed var(--ink)}
.ingredient__name{font-family:"Oswald",sans-serif;font-weight:500;font-size:8.5px;letter-spacing:.2px;height:14px}
.ingredient__icon{width:28px;height:28px;border:1.6px solid var(--ink);border-radius:50%;display:flex;align-items:center;justify-content:center}

.story{position:absolute;left:34px;top:84px;width:209px;height:159px;border:1px solid var(--ink);padding:11px 11px 0 11px;font-size:9.3px;line-height:11.9px;text-align:justify}
.story p + p{margin-top:7px}

/* centre */
.badge{position:absolute;left:325px;top:67px;width:116px;height:116px;border-radius:50%;background:var(--ink);border:5px solid var(--yellow);box-shadow:0 0 0 2px var(--ink);display:flex;align-items:center;justify-content:center;text-align:center}
.badge__name{font-family:"Oswald",sans-serif;font-weight:600;font-size:19px;line-height:20px;color:var(--white);letter-spacing:.5px}
.product{position:absolute;left:283px;top:194px;width:200px;text-align:center;white-space:nowrap}
.product__name{font-family:"Oswald",sans-serif;font-weight:700;font-size:25px;line-height:28px;color:var(--ink);letter-spacing:.6px}
.product__tag{font-family:"Montserrat",sans-serif;font-weight:600;font-size:6.6px;letter-spacing:2.4px;margin-top:4px}

/* right */
.brand{position:absolute;left:529px;top:44px}
.brand__title{font-family:"Oswald",sans-serif;font-weight:700;font-size:28px;line-height:30px;letter-spacing:-.3px}
.brand__co{font-family:"Oswald",sans-serif;font-weight:500;font-size:8.5px;margin-top:3px}
.brand__address{font-size:7.4px;line-height:10.5px;margin-top:2px}
.brand__rule{position:absolute;left:529px;top:121px;width:99px;border-top:1px solid var(--ink)}
.map{position:absolute;left:642px;top:58px;width:62px;height:56px;border-radius:40% 45% 50% 35%;background:var(--map)}
.pin{position:absolute;left:682px;top:44px}
.map__caption{position:absolute;left:683px;top:117px;font-family:"Oswald",sans-serif;font-weight:600;font-size:5.5px}

.facts{position:absolute;left:531px;top:134px;width:73px;height:109px;border:1px solid var(--ink);padding:4px 6px;display:flex;justify-content:center}
.facts__text{writing-mode:vertical-rl;transform:rotate(180deg);font-size:7.4px;line-height:9.5px;white-space:nowrap}
.facts__text b{font-weight:700}
.facts__text .loud{font-size:8.6px;font-weight:700}

.drinks{position:absolute;left:622px;top:199px;writing-mode:vertical-rl;transform:rotate(180deg);font-size:5.8px;white-space:nowrap}
.glass{position:absolute;left:636px;top:199px}

/* base info */
.specs{position:absolute;left:0;top:278px;width:767px;height:40px}
.spec{position:absolute;top:11px;font-size:10px;color:var(--white);border-bottom:1.5px solid var(--yellow);padding-bottom:1px;letter-spacing:.3px}
.spec--volume{left:328px}
.spec--ibu{left:408px}
.abv{position:absolute;left:368px;top:2px;width:33px;height:33px;border-radius:50%;background:var(--yellow);text-align:center;color:var(--ink)}
.abv__label{font-size:5.5px;display:block;margin-top:5px}
.abv__value{font-family:"Oswald",sans-serif;font-weight:600;font-size:12px;line-height:12px;display:block}
</style>
</head>
<body>

<section class="label label--one">
  <div class="texture texture--water" role="img" aria-label="Soft rippled water texture"></div>
  <svg class="chevron" width="74" height="46" viewBox="0 0 74 46" aria-hidden="true"><polygon points="0,0 74,0 37,28" fill="#f2cf00"/><polyline points="14,14 37,38 60,14" fill="none" stroke="#1c1c1c" stroke-width="6"/></svg>

  <div class="ingredients">
    <div class="ingredient"><span class="ingredient__name">WATER</span><span class="ingredient__icon"><svg width="10" height="14" viewBox="0 0 10 14"><path d="M5 0 C5 0 0 7 0 9 a5 5 0 0 0 10 0 C10 7 5 0 5 0Z" fill="#1c1c1c"/></svg></span></div>
    <div class="ingredient"><span class="ingredient__name">HOPS</span><span class="ingredient__icon"><svg width="12" height="14" viewBox="0 0 12 14"><path d="M6 0 L12 5 L9 12 L6 14 L3 12 L0 5Z" fill="#1c1c1c"/></svg></span></div>
    <div class="ingredient"><span class="ingredient__name">MALT</span><span class="ingredient__icon"><svg width="10" height="16" viewBox="0 0 10 16"><path d="M5 2 V16" stroke="#1c1c1c" stroke-width="1.2"/><ellipse cx="5" cy="3" rx="1.6" ry="2.6" fill="#1c1c1c"/><ellipse cx="2.5" cy="7" rx="1.6" ry="2.6" fill="#1c1c1c"/><ellipse cx="7.5" cy="7" rx="1.6" ry="2.6" fill="#1c1c1c"/><ellipse cx="2.5" cy="11" rx="1.6" ry="2.6" fill="#1c1c1c"/><ellipse cx="7.5" cy="11" rx="1.6" ry="2.6" fill="#1c1c1c"/></svg></span></div>
    <div class="ingredient"><span class="ingredient__name">YEAST</span><span class="ingredient__icon"><svg width="10" height="16" viewBox="0 0 10 16"><path d="M3.5 0 H6.5 V4 C9 6 10 9 10 16 H0 C0 9 1 6 3.5 4Z" fill="#1c1c1c"/></svg></span></div>
  </div>

  <div class="story">
    <p>The Tallow Creek brewery is ideally situated in Ashcombe, the hub of pristine North East Tasmania.<br>Our little patch is blessed with some of the greatest natural waterways, perfect for brewing the finest craft beers.</p>
    <p>Our Kelmoor Lager is smooth and easy to drink, with a distinctive golden straw like colour and a light body with a delicate bitterness. This is a crisp &amp; refreshing summer lager.</p>
  </div>

  <div class="badge"><span class="badge__name">TALLOW<br>CREEK</span></div>
  <div class="product"><div class="product__name">KELMOOR LAGER</div><div class="product__tag">HANDCRAFTED IN TASMANIA</div></div>

  <div class="brand"><div class="brand__title">KELMOOR</div><div class="brand__co">TALLOW CREEK BREWING CO</div><div class="brand__address">14 Ferris Lane, Ashcombe<br>Tasmania 7290</div></div>
  <div class="brand__rule"></div>
  <div class="map" role="img" aria-label="Outline map of Tasmania"></div>
  <svg class="pin" width="12" height="17" viewBox="0 0 12 17" aria-hidden="true"><path d="M6 0 a6 6 0 0 1 6 6 C12 10 6 17 6 17 C6 17 0 10 0 6 a6 6 0 0 1 6-6Z" fill="#f2cf00" stroke="#1c1c1c" stroke-width="1"/><circle cx="6" cy="6" r="2.2" fill="#1c1c1c"/></svg>
  <div class="map__caption">TASMANIA</div>

  <div class="facts"><div class="facts__text">TallowCreekBrewingCo<br><b>Head Brewer:</b> Sam Whitlow<br><br><b>Ingredients:</b> Water, Hops,<br>Malt and Yeast -<br><span class="loud">Nothing else !</span></div></div>
  <div class="drinks">Standard drinks</div>
  <svg class="glass" width="22" height="44" viewBox="0 0 22 44" aria-hidden="true"><path d="M0 0 H22 L20 44 H2Z" fill="#1c1c1c"/><text x="11" y="14" font-family="Arimo,sans-serif" font-size="8" fill="#fff" text-anchor="middle">1.3</text></svg>

  <div class="rule"></div><div class="stripe"></div><div class="band"></div><div class="notch"></div>
  <div class="specs"><span class="spec spec--volume">330 ml</span><span class="abv"><span class="abv__label">ABV</span><span class="abv__value">4.8%</span></span><span class="spec spec--ibu">IBU 22</span></div>
</section>

<section class="label label--two">
  <div class="texture texture--plain"></div>
  <div class="halftone" role="img" aria-label="Halftone dot burst behind the brewery badge"></div>
  <svg class="chevron" width="74" height="46" viewBox="0 0 74 46" aria-hidden="true"><polygon points="0,0 74,0 37,28" fill="#f2cf00"/><polyline points="14,14 37,38 60,14" fill="none" stroke="#1c1c1c" stroke-width="6"/></svg>

  <div class="ingredients">
    <div class="ingredient"><span class="ingredient__name">WATER</span><span class="ingredient__icon"><svg width="10" height="14" viewBox="0 0 10 14"><path d="M5 0 C5 0 0 7 0 9 a5 5 0 0 0 10 0 C10 7 5 0 5 0Z" fill="#1c1c1c"/></svg></span></div>
    <div class="ingredient"><span class="ingredient__name">HOPS</span><span class="ingredient__icon"><svg width="12" height="14" viewBox="0 0 12 14"><path d="M6 0 L12 5 L9 12 L6 14 L3 12 L0 5Z" fill="#1c1c1c"/></svg></span></div>
    <div class="ingredient"><span class="ingredient__name">MALT</span><span class="ingredient__icon"><svg width="10" height="16" viewBox="0 0 10 16"><path d="M5 2 V16" stroke="#1c1c1c" stroke-width="1.2"/><ellipse cx="5" cy="3" rx="1.6" ry="2.6" fill="#1c1c1c"/><ellipse cx="2.5" cy="7" rx="1.6" ry="2.6" fill="#1c1c1c"/><ellipse cx="7.5" cy="7" rx="1.6" ry="2.6" fill="#1c1c1c"/><ellipse cx="2.5" cy="11" rx="1.6" ry="2.6" fill="#1c1c1c"/><ellipse cx="7.5" cy="11" rx="1.6" ry="2.6" fill="#1c1c1c"/></svg></span></div>
    <div class="ingredient"><span class="ingredient__name">YEAST</span><span class="ingredient__icon"><svg width="10" height="16" viewBox="0 0 10 16"><path d="M3.5 0 H6.5 V4 C9 6 10 9 10 16 H0 C0 9 1 6 3.5 4Z" fill="#1c1c1c"/></svg></span></div>
  </div>

  <div class="story">
    <p>The Tallow Creek brewery is ideally situated in Ashcombe, the hub of pristine North East Tasmania.<br>Our little patch is blessed with some of the greatest natural waterways, perfect for brewing the finest craft beers.</p>
    <p>Our Kelmoor Lager is smooth and easy to drink, with a distinctive golden straw like colour and a light body with a delicate bitterness. This is a crisp &amp; refreshing summer lager.</p>
  </div>

  <div class="badge"><span class="badge__name">TALLOW<br>CREEK</span></div>
  <div class="product"><div class="product__name">KELMOOR LAGER</div><div class="product__tag">HANDCRAFTED IN TASMANIA</div></div>

  <div class="brand"><div class="brand__title">KELMOOR</div><div class="brand__co">TALLOW CREEK BREWING CO</div><div class="brand__address">14 Ferris Lane, Ashcombe<br>Tasmania 7290</div></div>
  <div class="brand__rule"></div>
  <div class="map" role="img" aria-label="Outline map of Tasmania"></div>
  <svg class="pin" width="12" height="17" viewBox="0 0 12 17" aria-hidden="true"><path d="M6 0 a6 6 0 0 1 6 6 C12 10 6 17 6 17 C6 17 0 10 0 6 a6 6 0 0 1 6-6Z" fill="#f2cf00" stroke="#1c1c1c" stroke-width="1"/><circle cx="6" cy="6" r="2.2" fill="#1c1c1c"/></svg>
  <div class="map__caption">TASMANIA</div>

  <div class="facts"><div class="facts__text">TallowCreekBrewingCo<br><b>Head Brewer:</b> Sam Whitlow<br><br><b>Ingredients:</b> Water, Hops,<br>Malt and Yeast -<br><span class="loud">Nothing else !</span></div></div>
  <div class="drinks">Standard drinks</div>
  <svg class="glass" width="22" height="44" viewBox="0 0 22 44" aria-hidden="true"><path d="M0 0 H22 L20 44 H2Z" fill="#1c1c1c"/><text x="11" y="14" font-family="Arimo,sans-serif" font-size="8" fill="#fff" text-anchor="middle">1.3</text></svg>

  <div class="rule"></div><div class="stripe"></div><div class="band band--marble" role="img" aria-label="Black and gold marbled band"></div><div class="notch"></div>
  <div class="specs"><span class="spec spec--volume">330 ml</span><span class="abv"><span class="abv__label">ABV</span><span class="abv__value">4.8%</span></span><span class="spec spec--ibu">IBU 22</span></div>
</section>

<section class="label label--three">
  <div class="texture texture--tiles" role="img" aria-label="Faint geometric triangle pattern"></div>
  <div class="halftone" role="img" aria-label="Halftone dot burst behind the brewery badge"></div>
  <svg class="chevron" width="74" height="46" viewBox="0 0 74 46" aria-hidden="true"><polygon points="0,0 74,0 37,28" fill="#f2cf00"/><polyline points="14,14 37,38 60,14" fill="none" stroke="#1c1c1c" stroke-width="6"/></svg>

  <div class="ingredients">
    <div class="ingredient"><span class="ingredient__name">WATER</span><span class="ingredient__icon"><svg width="10" height="14" viewBox="0 0 10 14"><path d="M5 0 C5 0 0 7 0 9 a5 5 0 0 0 10 0 C10 7 5 0 5 0Z" fill="#1c1c1c"/></svg></span></div>
    <div class="ingredient"><span class="ingredient__name">HOPS</span><span class="ingredient__icon"><svg width="12" height="14" viewBox="0 0 12 14"><path d="M6 0 L12 5 L9 12 L6 14 L3 12 L0 5Z" fill="#1c1c1c"/></svg></span></div>
    <div class="ingredient"><span class="ingredient__name">MALT</span><span class="ingredient__icon"><svg width="10" height="16" viewBox="0 0 10 16"><path d="M5 2 V16" stroke="#1c1c1c" stroke-width="1.2"/><ellipse cx="5" cy="3" rx="1.6" ry="2.6" fill="#1c1c1c"/><ellipse cx="2.5" cy="7" rx="1.6" ry="2.6" fill="#1c1c1c"/><ellipse cx="7.5" cy="7" rx="1.6" ry="2.6" fill="#1c1c1c"/><ellipse cx="2.5" cy="11" rx="1.6" ry="2.6" fill="#1c1c1c"/><ellipse cx="7.5" cy="11" rx="1.6" ry="2.6" fill="#1c1c1c"/></svg></span></div>
    <div class="ingredient"><span class="ingredient__name">YEAST</span><span class="ingredient__icon"><svg width="10" height="16" viewBox="0 0 10 16"><path d="M3.5 0 H6.5 V4 C9 6 10 9 10 16 H0 C0 9 1 6 3.5 4Z" fill="#1c1c1c"/></svg></span></div>
  </div>

  <div class="story">
    <p>The Tallow Creek brewery is ideally situated in Ashcombe, the hub of pristine North East Tasmania.<br>Our little patch is blessed with some of the greatest natural waterways, perfect for brewing the finest craft beers.</p>
    <p>Our Kelmoor Lager is smooth and easy to drink, with a distinctive golden straw like colour and a light body with a delicate bitterness. This is a crisp &amp; refreshing summer lager.</p>
  </div>

  <div class="badge"><span class="badge__name">TALLOW<br>CREEK</span></div>
  <div class="product"><div class="product__name">KELMOOR LAGER</div><div class="product__tag">HANDCRAFTED IN TASMANIA</div></div>

  <div class="brand"><div class="brand__title">KELMOOR</div><div class="brand__co">TALLOW CREEK BREWING CO</div><div class="brand__address">14 Ferris Lane, Ashcombe<br>Tasmania 7290</div></div>
  <div class="brand__rule"></div>
  <div class="map" role="img" aria-label="Outline map of Tasmania"></div>
  <svg class="pin" width="12" height="17" viewBox="0 0 12 17" aria-hidden="true"><path d="M6 0 a6 6 0 0 1 6 6 C12 10 6 17 6 17 C6 17 0 10 0 6 a6 6 0 0 1 6-6Z" fill="#f2cf00" stroke="#1c1c1c" stroke-width="1"/><circle cx="6" cy="6" r="2.2" fill="#1c1c1c"/></svg>
  <div class="map__caption">TASMANIA</div>

  <div class="facts"><div class="facts__text">TallowCreekBrewingCo<br><b>Head Brewer:</b> Sam Whitlow<br><br><b>Ingredients:</b> Water, Hops,<br>Malt and Yeast -<br><span class="loud">Nothing else !</span></div></div>
  <div class="drinks">Standard drinks</div>
  <svg class="glass" width="22" height="44" viewBox="0 0 22 44" aria-hidden="true"><path d="M0 0 H22 L20 44 H2Z" fill="#1c1c1c"/><text x="11" y="14" font-family="Arimo,sans-serif" font-size="8" fill="#fff" text-anchor="middle">1.3</text></svg>

  <div class="rule"></div><div class="stripe"></div><div class="band"></div><div class="notch"></div>
  <div class="specs"><span class="spec spec--volume">330 ml</span><span class="abv"><span class="abv__label">ABV</span><span class="abv__value">4.8%</span></span><span class="spec spec--ibu">IBU 22</span></div>
</section>

</body>
</html>
```